Brindle Structures Construction Company Seeking Modern Website

We are a small construction company wanting to create a web presence. We don't have much in the way of current content but will get photos as they come in. Attached is a picture of our business card.
The pages we would like on the menu are:
Home
Portfolio
Product Specs
Testimonials
Our Process
Contact
Some designs we like are:
http://www.tovenquarnsheds.example/
http://www.qzrsheds.example/
http://pannowsheds.example/
http://wistenhalls.example/
Not much requirements other than that so feel free to be creative!
Updates
Target Market(s)
Construction
Commercial and Residential Buildings
Industry/Entity Type
Construction Company
Number of Pages Required
5+ page
Look and feel

```html
<!DOCTYPE html>
<html lang="en">
<head>
<meta charset="utf-8">
<title>Brindle Structures</title>
<link href="https://fonts.googleapis.com/css2?family=Roboto:wght@300;400;500;700;900&display=swap" rel="stylesheet">
<style>
:root{
  --red:#e2301f;
  --red-dark:#b71d13;
  --black:#0c0c0c;
  --ink:#222;
  --muted:#666;
  --orange:#f26522;
  --green:#3aa640;
  --blue:#12a9e0;
  --crimson:#d7262c;
  --white:#fff;
}
*{box-sizing:border-box;margin:0;padding:0}
html,body{width:1200px;height:3475px;overflow:hidden}
body{position:relative;font-family:"Roboto",Arial,sans-serif;color:var(--ink);background:var(--white)}
.abs{position:absolute}

/* header */
.topbar{left:0;top:0;width:1200px;height:46px;background:var(--black)}
.brand{left:258px;top:6px;font-size:34px;font-weight:700;color:var(--white);letter-spacing:.5px;line-height:36px}
.social{display:flex;gap:10px}
.social span{width:24px;height:24px;border:2px solid currentColor;border-radius:50%;display:block}
.top-social{left:660px;top:11px;color:var(--white)}
.call{left:820px;top:6px;color:var(--white);text-align:center;line-height:1}
.call small{font-size:11px;display:block;margin-bottom:4px}
.call strong{font-size:22px;font-weight:700}
.nav{left:0;top:46px;width:1200px;height:38px;background:var(--white);display:flex;gap:30px;padding-left:505px;align-items:center}
.nav a{font-size:12px;font-weight:500;color:#333;text-decoration:none;position:relative}
.nav a.active{color:var(--red)}
.nav a.active::after{content:"";position:absolute;left:0;right:0;bottom:-11px;height:3px;background:var(--red)}

/* hero */
.hero{left:0;top:0;width:1200px;height:1240px}
.welcome{left:620px;top:520px;width:310px;color:var(--white)}
.welcome h2{text-align:right;font-weight:500;font-size:18px;line-height:1.1}
.welcome h2 b{display:block;font-size:26px;font-weight:700;margin-bottom:18px}
.welcome p{font-size:11.5px;line-height:1.6;text-align:justify}
.portfolio-title{left:268px;top:712px;color:var(--white);font-size:18px;font-weight:500;line-height:1}
.portfolio-title b{display:block;font-size:30px;font-weight:700}
.slider{left:271px;top:772px;width:658px;height:360px;background:linear-gradient(160deg,#d9cfa8,#b9a77d 55%,#4f7a36)}
.arrow{width:32px;height:32px;border-radius:50%;background:var(--black);display:flex;align-items:center;justify-content:center}
.thumbs{left:271px;top:1134px;width:658px;height:70px;display:flex;gap:3px}
.thumbs div{flex:1;height:70px}

/* product specs */
.specs{left:0;top:1240px;width:1200px;height:498px;background:radial-gradient(circle at 50% 40%,#f7f7f7,#dcdcdc)}
.section-title{width:1200px;text-align:center;font-size:46px;font-weight:300;letter-spacing:.5px;line-height:1}
.section-title b{font-weight:900}
.spec{width:200px;text-align:center;top:1407px}
.spec .diamond{width:96px;height:96px;margin:0 auto;transform:rotate(45deg);border:4px solid #fff;box-shadow:0 0 0 1px #ccc}
.spec h3{font-size:12px;font-weight:700;margin-top:44px;line-height:1.3}
.spec h3 span{display:block;font-weight:400}
.spec p{font-size:11px;color:var(--muted);line-height:1.5;margin:14px auto 0;width:150px}
.btn{display:inline-block;background:var(--red);color:#fff;font-size:10px;font-weight:700;padding:6px 12px;margin-top:14px;border-radius:2px}

/* dark section */
.dark{left:0;top:1738px;width:1200px;height:1499px;background:linear-gradient(180deg,#3c3c3c 0%,#1c1c1c 40%,#0d0d0d 100%)}
.t-title{left:0;top:1812px;width:1200px;text-align:center;color:#fff;font-weight:300;font-size:48px;letter-spacing:1px;line-height:1}
.t-name{left:0;top:1884px;width:1200px;text-align:center;color:#fff;font-weight:700;font-size:17px}
.t-text{left:316px;top:1916px;width:568px;text-align:center;color:#ddd;font-size:11px;line-height:1.75}
.t-arrow{width:26px;height:26px;border:2px solid #fff;transform:rotate(45deg)}
.dots{left:585px;top:2034px;display:flex;gap:4px}
.dots i{width:7px;height:7px;border-radius:50%;border:1px solid #fff;display:block}
.dots i.on{background:#fff}
.step{color:#fff;text-align:center;width:190px}
.step .num{font-size:56px;font-weight:500;line-height:1}
.step h4{font-size:17px;font-weight:400;margin:2px 0 8px}
.step p{font-size:10px;line-height:1.45}
.step .more{display:inline-block;border:1px solid #fff;font-size:9px;padding:4px 12px;margin-top:8px}
.process-title{left:300px;top:2190px;width:280px;text-align:center;color:#fff;font-size:40px;font-weight:300;line-height:1;transform:rotate(-45deg);transform-origin:center;white-space:nowrap}
.process-title b{font-weight:900}

/* contact */
.contact-title{left:0;top:2680px;color:#fff}
.field label,.label{display:block;font-size:10px;color:#fff;margin-bottom:5px}
.field label i,.label i{color:var(--red);font-style:normal}
.input{background:#fff;height:35px;border-radius:2px}
.date{display:flex;align-items:center;justify-content:space-between;padding:0 8px;font-size:11px;color:#333}
.date span{width:22px;height:20px;border:2px solid var(--red);border-top-width:6px;border-radius:2px}
.checks{left:343px;top:3141px;display:flex;gap:50px;font-size:9px;color:#aaa}
.checks span{display:flex;align-items:center;gap:8px}
.checks span::before{content:"";width:9px;height:9px;background:#fff;display:block}
.submit{left:343px;top:3168px;width:62px;height:24px;background:var(--red);color:#fff;font-size:11px;font-weight:700;display:flex;align-items:center;justify-content:center;border-radius:2px}

/* footer */
.footer h5{font-size:13px;font-weight:700;color:#222;top:3280px}
.footer p{font-size:10.5px;color:#555;line-height:1.55;top:3312px;width:160px}
.footer-social{left:792px;top:3310px;color:#333}
.footer-rule{left:269px;top:3422px;width:662px;height:1px;background:#ddd}
.copyright{left:269px;top:3442px;font-size:9px;color:#444}
</style>
</head>
<body>

<svg class="abs hero" width="1200" height="1240" viewBox="0 0 1200 1240">
  <defs>
    <linearGradient id="redFill" x1="0" y1="0" x2="0" y2="1">
      <stop offset="0" stop-color="#ea3a26"/><stop offset="1" stop-color="#c0201a"/>
    </linearGradient>
  </defs>
  <rect x="487" y="83" width="713" height="392" fill="#e9eaea" role="img" aria-label="Photo: hands holding a model house"/>
  <polygon points="0,83 487,83 255,475 0,475" fill="#7a5a3a" role="img" aria-label="Photo: hard hat, tape measure and building tools"/>
  <polygon points="498,266 741,475 475,730 255,475" fill="#6fa74a" role="img" aria-label="Photo: house on a green field under blue sky"/>
  <polygon points="0,475 255,475 475,730 0,1205" fill="#6e7f4c" role="img" aria-label="Photo: smiling client with a small house model"/>
  <polygon points="741,475 1200,475 1200,1240 0,1240 0,1205" fill="url(#redFill)"/>
</svg>

<div class="abs topbar"></div>
<div class="abs brand">Brindle Structures</div>
<div class="abs social top-social"><span></span><span></span><span></span><span></span></div>
<div class="abs call"><small>Call Us Today!</small><strong>000.000.0000</strong></div>
<nav class="abs nav">
  <a class="active">HOME</a><a>PORTFOLIO</a><a>PRODUCT SPECS</a><a>TESTIMONIALS</a><a>OUR PROCESS</a><a>CONTACT</a>
</nav>

<div class="abs welcome">
  <h2>WELCOME TO<b>BRINDLE STRUCTURES</b></h2>
  <p>Lorem Ipsum has been the industry's standard dummy text ever since the 1500s, when an unknown printer took a galley of type and scrambled it to make a type specimen book. It has survived not only five centuries, but also the leap into electronic typesetting, remaining essentially unchanged. Lorem Ipsum is simply dummy text of the Lorem Ipsum has been the industry's standard dummy text ever since the 1500s, when an unknown printer took a galley of type and</p>
</div>
<div class="abs portfolio-title">OUR<b>PORTFOLIO</b></div>
<div class="abs slider" role="img" aria-label="Portfolio photo: couple sitting in front of their new home"></div>
<div class="abs arrow" style="left:280px;top:935px"><svg width="12" height="12" viewBox="0 0 12 12"><path d="M8 1 3 6l5 5" stroke="#fff" stroke-width="2.4" fill="none"/></svg></div>
<div class="abs arrow" style="left:888px;top:935px"><svg width="12" height="12" viewBox="0 0 12 12"><path d="m4 1 5 5-5 5" stroke="#fff" stroke-width="2.4" fill="none"/></svg></div>
<div class="abs thumbs">
  <div style="background:#c9c3a4" role="img" aria-label="Thumbnail: couple"></div>
  <div style="background:#a07a62" role="img" aria-label="Thumbnail: family"></div>
  <div style="background:#c9b9a8" role="img" aria-label="Thumbnail: couple outdoors"></div>
  <div style="background:#7d8ea3" role="img" aria-label="Thumbnail: house exterior"></div>
  <div style="background:#8f9a84" role="img" aria-label="Thumbnail: house and lawn"></div>
  <div style="background:#9aa0a6" role="img" aria-label="Thumbnail: house at dusk"></div>
</div>

<section class="abs specs"></section>
<svg class="abs" style="left:556px;top:1240px" width="88" height="40" viewBox="0 0 88 40"><polygon points="0,0 88,0 44,39" fill="#c0201a"/></svg>
<h2 class="abs section-title" style="left:0;top:1305px"><b>PRODUCT</b> SPECS</h2>
<div class="abs spec" style="left:236px"><div class="diamond" style="background:#b5542b" role="img" aria-label="Photo: worker on a building frame"></div><h3>Brindle<span>Advantages</span></h3><p>Lorem Ipsum has been the industry's standard dummy text ever since the 1500s.</p><span class="btn">View More</span></div>
<div class="abs spec" style="left:410px"><div class="diamond" style="background:#4b4a50" role="img" aria-label="Photo: post frame building"></div><h3>Post Frame<span>Advantages</span></h3><p>Lorem Ipsum has been the industry's standard dummy text ever since the 1500s.</p><span class="btn">View More</span></div>
<div class="abs spec" style="left:588px"><div class="diamond" style="background:#a79a72" role="img" aria-label="Photo: builders on site"></div><h3>Building<span>Process</span></h3><p>Lorem Ipsum has been the industry's standard dummy text ever since the 1500s.</p><span class="btn">View More</span></div>
<div class="abs spec" style="left:764px"><div class="diamond" style="background:#5d7a3e" role="img" aria-label="Photo: finished building"></div><h3>Building<span>Features</span></h3><p>Lorem Ipsum has been the industry's standard dummy text ever since the 1500s.</p><span class="btn">View More</span></div>

<section class="abs dark"></section>
<svg class="abs" style="left:0;top:1738px" width="1200" height="1499" viewBox="0 0 1200 1499">
  <polygon points="556,0 644,0 600,42" fill="#dedede"/>
  <polygon points="1085,30 1200,30 1200,490 970,270" fill="#3f5f86" role="img" aria-label="Photo: smiling client"/>
  <polygon points="0,780 200,1010 0,1230" fill="#6a4030" role="img" aria-label="Photo: brick house"/>
</svg>
<h2 class="abs t-title">TESTIMONIALS</h2>
<div class="abs t-name">NAME HOME</div>
<p class="abs t-text">Lorem Ipsum has been the industry's standard dummy text ever since the 1500s, when an unknown printer took a galley of type and scrambled it to make a type specimen book. It has survived not only five centuries, but also the leap into electronic typesetting, remaining essentially unchanged. Lorem Ipsum has been the industry's standard dummy text ever since the 1500s, when an unknown printer took a galley of type and scrambled it to make a type specimen book. It has survived five centuries, remaining unchanged. Lorem Ipsum is simply dummy text of the</p>
<div class="abs t-arrow" style="left:286px;top:1937px"></div>
<div class="abs t-arrow" style="left:888px;top:1937px"></div>
<div class="abs dots"><i class="on"></i><i></i><i></i><i></i></div>

<svg class="abs" style="left:0;top:2070px" width="1200" height="580" viewBox="0 2070 1200 580">
  <polygon points="600,2080 737,2219 600,2356 463,2219" fill="var(--orange)"/>
  <polygon points="463,2226 600,2363 463,2500 326,2363" fill="var(--crimson)"/>
  <polygon points="737,2226 874,2363 737,2500 600,2363" fill="var(--green)"/>
  <polygon points="600,2365 737,2502 600,2639 463,2502" fill="var(--blue)"/>
</svg>
<div class="abs process-title"><b>OUR</b> PROCESS</div>
<div class="abs step" style="left:505px;top:2115px"><div class="num">1</div><h4>Brindle Design</h4><p>Lorem Ipsum has been the industry's standard dummy text ever since the 1500s, when an unknown printer took a galley of type</p><span class="more">Find More</span></div>
<div class="abs step" style="left:368px;top:2258px"><div class="num">4</div><h4>Material Design</h4><p>Lorem Ipsum has been the industry's standard dummy text ever since the 1500s, when an unknown printer took a galley of type</p><span class="more">Find More</span></div>
<div class="abs step" style="left:642px;top:2258px"><div class="num">2</div><h4>Frame Design</h4><p>Lorem Ipsum has been the industry's standard dummy text ever since the 1500s, when an unknown printer took a galley of type</p><span class="more">Find More</span></div>
<div class="abs step" style="left:505px;top:2402px"><div class="num">3</div><h4>Building Design</h4><p>Lorem Ipsum has been the industry's standard dummy text ever since the 1500s, when an unknown printer took a galley of type</p><span class="more">Find More</span></div>

<h2 class="abs section-title contact-title"><b>CONTACT</b> US</h2>
<div class="abs field" style="left:343px;top:2764px;width:248px"><label>Your Name <i>*</i></label><div class="input"></div></div>
<div class="abs field" style="left:609px;top:2764px;width:248px"><label>Your Phone <i>*</i></label><div class="input"></div></div>
<div class="abs field" style="left:343px;top:2827px;width:248px"><label>Your Email <i>*</i></label><div class="input"></div></div>
<div class="abs field" style="left:609px;top:2827px;width:248px"><label>City <i>*</i></label><div class="input"></div></div>
<div class="abs field" style="left:343px;top:2894px;width:514px"><label>Comment <i>*</i></label><div class="input" style="height:120px"></div></div>
<div class="abs label" style="left:343px;top:3050px">Preferred Consultation Date <i>*</i></div>
<div class="abs input date" style="left:343px;top:3068px;width:116px">01/17/2015<span></span></div>
<div class="abs input date" style="left:473px;top:3068px;width:116px">01/17/2015<span></span></div>
<div class="abs label" style="left:343px;top:3120px">Availability <i>*</i></div>
<div class="abs checks"><span>Morning (8a-12pm)</span><span>Afternoon (12pm-5pm)</span><span>All day</span></div>
<div class="abs submit">Submit</div>

<footer class="footer">
  <h5 class="abs" style="left:269px">ABOUT</h5>
  <p class="abs" style="left:269px;width:140px">Lorem Ipsum has been the industry's standard dummy text ever since the 1500s, when an unknown printer took a galley of type and scrambled it to make a type specimen book. It has</p>
  <h5 class="abs" style="left:443px">OUR ADDRESS</h5>
  <p class="abs" style="left:443px">Corvale Contractors<br>P.O. Box 240<br>Alderford IN 40000</p>
  <h5 class="abs" style="left:619px">CONTACT INFO</h5>
  <p class="abs" style="left:619px;width:170px;font-size:9.5px"><b>Phone:</b> 000.000.0000<br><b>Fax:</b> 000.000.0000<br><b>E-mail:</b> info@brindlestructures.example</p>
  <h5 class="abs" style="left:792px">GET SOCIAL</h5>
  <div class="abs social footer-social"><span></span><span></span><span></span><span></span></div>
  <div class="abs footer-rule"></div>
  <div class="abs copyright">Copyright © 2015 Brindle Structures Co.</div>
</footer>

</body>
</html>
```